business card for dental office

We need a business card design for an existing company follwing information we need on the card:
Teodor L Vanwick, DDS
4263 Harlowe Court
Springfield, VA 22150
Ph: 703-555-0142 Fax:703-555-0187
www.grinvalemont.example info@grinvalemont.example
second side
Appointment
For
Date: day:
Time
if you are unable to keep your appointment, please contact us 24 hours in advance.
Note: Logo is attached to use with the card
Thanks
Industry/Entity Type
Dental Clinic
Contact Information for Business Card
Teodor L Vanwick, DDS
4263 Harlowe Court
Springfield, VA 22150
second side
Appointment
For
Date: day:
Time
Thanks

```html
<!DOCTYPE html>
<html lang="en">
<head>
<meta charset="utf-8">
<title>Grinvale Dental Associates – Business Card</title>
<link href="https://fonts.googleapis.com/css2?family=Didact+Gothic&family=Roboto+Condensed:ital,wght@0,300;0,400;1,300&family=Marcellus&family=Josefin+Sans:wght@400;600&display=swap" rel="stylesheet">
<style>
  :root{
    --ink-purple:#261452;
    --sky:#4bb3e2;
    --accent:#00aeef;
    --brand-navy:#1e3a6e;
    --footer-navy:#2e2f6b;
    --rule:#2a2d6e;
    --paper:#ffffff;
    --stage-dark:#000000;
  }
  *{margin:0;padding:0;box-sizing:border-box}
  html,body{width:1200px;height:1120px;overflow:hidden;background:var(--paper)}
  .canvas{position:relative;width:1200px;height:1120px;background:var(--paper)}
  .stage-band{position:absolute;left:0;top:557px;width:1200px;height:563px;background:var(--stage-dark)}
  .card{position:absolute;left:106px;width:960px;height:549px;overflow:hidden;background:var(--paper)}
  .card-front{top:0}
  .card-back{top:571px}
  .card svg.shapes{position:absolute;inset:0}
  .card div,.card address{white-space:nowrap}

  .doctor-name{position:absolute;left:78px;top:64px;font-family:"Didact Gothic",sans-serif;font-size:43px;color:#fff;letter-spacing:.5px}
  .doctor-title{position:absolute;left:141px;top:117px;font-family:"Roboto Condensed",sans-serif;font-style:italic;font-weight:300;font-size:19px;color:var(--accent)}
  .contact{position:absolute;left:120px;font-family:"Roboto Condensed",sans-serif;font-weight:300;color:#fff}
  .contact-email{top:211px;font-size:26px}
  .contact-web{top:277px;font-size:26px}
  .contact-phone{top:356px;font-size:28px;letter-spacing:2px;left:127px}
  .contact-fax{top:423px;font-size:28px;letter-spacing:2px;left:127px}

  .brand{position:absolute;font-family:"Marcellus",serif;color:var(--brand-navy);display:flex;align-items:center;gap:14px}
  .brand-dot{width:34px;height:34px;border-radius:50%;background:var(--sky);flex:none}
  .brand-name{font-size:44px;line-height:1}
  .brand-sub{display:block;font-size:18px;letter-spacing:10px;margin-top:8px}
  .card-front .brand{left:476px;top:198px}
  .card-back .brand{left:80px;top:88px}

  .address{position:absolute;left:629px;top:438px;font-family:"Marcellus",serif;font-size:28px;line-height:27px;color:#fff;letter-spacing:.5px;font-style:normal}

  .appointment-title{position:absolute;left:512px;top:160px;font-family:"Josefin Sans",sans-serif;font-weight:600;font-size:62px;letter-spacing:-1px;color:#fff;line-height:1}
  .field-label{position:absolute;font-family:"Didact Gothic",sans-serif;font-size:30px;color:var(--brand-navy)}
  .small-note{position:absolute;font-family:"Roboto Condensed",sans-serif;font-style:italic;font-weight:300;color:var(--accent)}
  .day-name{font-size:13px;width:84px;text-align:center;top:315px}
  .tick-note{left:580px;top:365px;font-size:11px}
  .ampm{left:302px;top:395px;font-size:24px}
  .date-hint{font-size:21px;top:327px;width:50px;text-align:center;color:#9aa6c8}
  .footer-note{position:absolute;left:0;top:493px;width:960px;height:56px;background:var(--footer-navy);color:#fff;font-family:"Josefin Sans",sans-serif;font-size:22px;display:flex;align-items:center;justify-content:center;letter-spacing:-.2px;white-space:nowrap;overflow:hidden}
</style>
</head>
<body>
<div class="canvas">
  <div class="stage-band"></div>

  <section class="card card-front">
    <svg class="shapes" width="960" height="549" viewBox="0 0 960 549">
      <path d="M505 0 H960 V72 C820 108 640 92 505 32 Z" fill="var(--sky)"/>
      <path d="M505 32 C640 92 820 108 960 72" fill="none" stroke="var(--ink-purple)" stroke-width="7"/>
      <path d="M270 549 C450 440 700 370 960 410 V549 Z" fill="var(--ink-purple)"/>
      <path d="M296 549 C470 452 710 388 960 424 V549 Z" fill="var(--sky)"/>
      <path d="M0 0 H502 C505 200 460 400 198 549 H0 Z" fill="var(--ink-purple)"/>
      <path d="M58 110 C58 90 62 72 72 64 L478 62 C484 62 482 68 476 66" fill="none" stroke="#fff" stroke-width="3"/>
      <line x1="48" y1="333" x2="393" y2="333" stroke="var(--accent)" stroke-width="3"/>
      <g fill="#fff">
        <circle cx="77" cy="226" r="28"/><circle cx="77" cy="294" r="28"/>
        <circle cx="77" cy="372" r="28"/><circle cx="77" cy="440" r="28"/>
      </g>
      <g fill="none" stroke="var(--ink-purple)" stroke-width="2.5">
        <rect x="62" y="216" width="30" height="20" rx="2"/>
        <path d="M62 218 L77 229 L92 218"/>
        <circle cx="77" cy="294" r="15"/>
        <ellipse cx="77" cy="294" rx="6" ry="15"/>
        <line x1="62" y1="294" x2="92" y2="294"/>
        <line x1="64" y1="287" x2="90" y2="287"/><line x1="64" y1="301" x2="90" y2="301"/>
        <rect x="63" y="430" width="8" height="22" rx="2"/>
        <rect x="71" y="433" width="21" height="19" rx="2"/>
        <rect x="76" y="424" width="11" height="9"/>
      </g>
      <path d="M65 360 C62 372 72 386 86 387 L90 380 L83 374 L78 378 C74 376 71 372 70 368 L74 363 L69 356 Z" fill="var(--ink-purple)"/>
      <g fill="var(--ink-purple)">
        <rect x="76" y="437" width="3" height="3"/><rect x="81" y="437" width="3" height="3"/><rect x="86" y="437" width="3" height="3"/>
        <rect x="76" y="442" width="3" height="3"/><rect x="81" y="442" width="3" height="3"/><rect x="86" y="442" width="3" height="3"/>
      </g>
      <ellipse cx="594" cy="491" rx="23" ry="7" fill="none" stroke="var(--ink-purple)" stroke-width="3"/>
      <path d="M594 490 C584 474 578 466 578 458 A16 16 0 0 1 610 458 C610 466 604 474 594 490 Z" fill="var(--ink-purple)"/>
      <circle cx="594" cy="457" r="5" fill="#fff"/>
      <line x1="567" y1="510" x2="906" y2="510" stroke="var(--ink-purple)" stroke-width="2"/>
      <circle cx="567" cy="510" r="2.5" fill="var(--ink-purple)"/><circle cx="906" cy="510" r="2.5" fill="var(--ink-purple)"/>
    </svg>

    <div class="doctor-name">Teodor L Vanwick</div>
    <div class="doctor-title">DDS (Doctor of Dental Surgery)</div>
    <div class="contact contact-email">info@grinvalemont.example</div>
    <div class="contact contact-web">www.grinvalemont.example</div>
    <div class="contact contact-phone">703-555-0142</div>
    <div class="contact contact-fax">703-555-0187</div>

    <div class="brand">
      <span class="brand-dot"></span>
      <div><span class="brand-name">Grinvale Dental</span><span class="brand-sub">associates</span></div>
    </div>

    <address class="address">4263 Harlowe Court<br>Springfield, VA 22150</address>
  </section>

  <section class="card card-back">
    <svg class="shapes" width="960" height="549" viewBox="0 0 960 549">
      <path d="M500 141 H960 V225 H474 C486 206 492 170 500 141 Z" fill="var(--accent)"/>
      <line x1="115" y1="299" x2="914" y2="299" stroke="var(--rule)" stroke-width="2"/>
      <g fill="none" stroke="var(--rule)" stroke-width="2">
        <rect x="147" y="330" width="151" height="30"/>
        <line x1="198" y1="330" x2="198" y2="360"/><line x1="248" y1="330" x2="248" y2="360"/>
        <rect x="437" y="330" width="403" height="30"/>
        <line x1="504" y1="330" x2="504" y2="360"/><line x1="571" y1="330" x2="571" y2="360"/>
        <line x1="638" y1="330" x2="638" y2="360"/><line x1="705" y1="330" x2="705" y2="360"/>
        <line x1="772" y1="330" x2="772" y2="360"/>
      </g>
      <rect x="728" y="364" width="37" height="14" fill="none" stroke="var(--accent)" stroke-width="2"/>
      <path d="M738 371 L744 375 L755 367" fill="none" stroke="var(--accent)" stroke-width="2"/>
      <line x1="134" y1="418" x2="384" y2="418" stroke="var(--rule)" stroke-width="2"/>
    </svg>

    <div class="brand">
      <span class="brand-dot"></span>
      <div><span class="brand-name">Grinvale Dental</span><span class="brand-sub">associates</span></div>
    </div>

    <div class="appointment-title">Appointment</div>

    <div class="field-label" style="left:57px;top:270px">For:</div>
    <div class="field-label" style="left:57px;top:328px">Date:</div>
    <div class="small-note date-hint" style="left:148px">mm</div>
    <div class="small-note date-hint" style="left:198px">dd</div>
    <div class="small-note date-hint" style="left:248px">yy</div>
    <div class="field-label" style="left:368px;top:328px">Day:</div>
    <div class="small-note day-name" style="left:437px">Mon</div>
    <div class="small-note day-name" style="left:504px">Tue</div>
    <div class="small-note day-name" style="left:571px">Wed</div>
    <div class="small-note day-name" style="left:638px">Thu</div>
    <div class="small-note day-name" style="left:705px">Fri</div>
    <div class="small-note day-name" style="left:772px">Sat</div>
    <div class="small-note tick-note">Please tick the appropriate box</div>
    <div class="field-label" style="left:57px;top:385px">Time:</div>
    <div class="small-note ampm">am/pm</div>

    <div class="footer-note">If you are unable to keep your appointment, please contact us 24 hours in advance.</div>
  </section>
</div>
</body>
</html>
```